Business Card Design Project

looking for a stylish and simple double sided business card.
I am an artist - specialising in fashion illustration, portraits and murals.
the front should be simply my name and tag:

D A V E R U
Living in colour

My preference is for a Black background with DAVERU in red or embossed.
Living in colour in White or multi-coloured.

the back will have detail:

Personalised Art
Portraits, Murals, Fashion Illustration

0487 312 560
daveru@daveru.com.au
www.daveru.com.au

Target Market(s)

Adults that are based in western speaking countries who have an appreciation for art and design. Portraits and wall art
Business owners who may need personalised all art for their business space. Murals and personalised canvass.
People in the fashion industry, who may require fashion illustrations.

Industry/Entity Type

Fashion

Requirements
Must have
• BOLD but simple at the same time, timeless modern element to it.
Nice to have
• simple lettering
Should not have
• Not too busy or wordy,

```html
<!DOCTYPE html>
<html lang="en">
<head>
<meta charset="utf-8">
<title>DAVERU — Business Card Back</title>
<link rel="stylesheet" href="https://fonts.googleapis.com/css2?family=Roboto:wght@300;400&display=swap">
<style>
  :root {
    --card-black: #000000;
    --ink-white: #ffffff;
    --accent-red: #ff0000;
    --stripe-pale: #fbe9e9;
    --stripe-mist: #e6f2f2;
  }
  * { margin: 0; padding: 0; box-sizing: border-box; }
  html, body {
    width: 1200px;
    height: 720px;
    overflow: hidden;
    background: var(--card-black);
  }
  .card {
    position: relative;
    width: 1200px;
    height: 720px;
    background: var(--card-black);
    color: var(--ink-white);
    font-family: "Roboto", "Helvetica Neue", Arial, sans-serif;
    font-weight: 300;
  }
  .accent-stripe {
    position: absolute;
    left: 0;
    top: 97px;
    width: 955px;
    height: 12px;
    background: linear-gradient(90deg,
      var(--accent-red) 0%,
      #ff2a2a 22%,
      var(--stripe-pale) 50%,
      var(--ink-white) 58%,
      var(--stripe-mist) 68%,
      #6c7474 85%,
      var(--card-black) 100%);
  }
  .services {
    position: absolute;
    left: 0;
    right: 0;
    top: 246px;
    list-style: none;
    text-align: center;
    font-size: 46px;
    letter-spacing: 2px;
    line-height: 1;
  }
  .services li { height: 62px; }
  .services li + li { margin-top: 0; }
  .services .highlight { color: var(--accent-red); }
  .contact {
    position: absolute;
    left: 0;
    right: 0;
    top: 656px;
    font-size: 37px;
    line-height: 1;
  }
  .contact span { position: absolute; top: 0; white-space: nowrap; }
  .contact .web { left: 26px; }
  .contact .phone { left: 443px; letter-spacing: 4px; }
  .contact .email { right: 26px; }
</style>
</head>
<body>
  <main class="card">
    <div class="accent-stripe" aria-hidden="true"></div>

    <ul class="services">
      <li>FASHION&nbsp; ILL<span class="highlight">U</span>ST<span class="highlight">R</span>ATION</li>
      <li>PORTR<span class="highlight">A</span>ITS</li>
      <li>P<span class="highlight">E</span>RSONALISE<span class="highlight">D</span>&nbsp; ART</li>
      <li>MUR<span class="highlight">A</span>LS</li>
    </ul>

    <footer class="contact">
      <span class="web">www.daveru.com.au</span>
      <span class="phone">0487 312 560</span>
      <span class="email">daveru@daveru.com.au</span>
    </footer>
  </main>
</body>
</html>
```